Clean and sophisticated website for Velmarudin

Velmarudin is a group of enthusiasts offering education, welfare, health and publications. The organization is going through a re branding phase and looking to design a new website for velmarudin.org. The current landing page will be replaced by the new website. Looking for a creative design that could be converted into a responsive wordpress theme and integrated on the website.

The new website will have all the content of the 4 different sites that are accessible from the landing page.

Target Market(s)

Donors, information seekers, and students.

Industry/Entity Type

Non-Profit

Number of Pages Required

5+ page

Font styles to use
Sans Serif

Requirements
Must have
• Sophisticated look.
• Multi lingual interface (English + Urdu)
• Great User experience and Easy Navigation
• SEO friendly
• Prominent sections for 4 main categories
• Responsive design
Nice to have
• banners
• Parallax
• Call to action buttons
• simple clean design
Should not have
• Dark Colors
• Busy portal style look
• Flash
• cluttered design

```html
<!DOCTYPE html>
<html lang="en">
<head>
<meta charset="utf-8">
<title>Velmarudin</title>
<link rel="stylesheet" href="https://fonts.googleapis.com/css2?family=Raleway:wght@500;600;700;800&family=Open+Sans:wght@400;600;700&display=swap">
<style>
:root{
  --blue:#1e6fbf;
  --blue-dark:#195fa6;
  --orange:#f05a28;
  --green:#3ab54a;
  --ink:#333333;
  --muted:#777777;
  --light:#f4f4f5;
  --white:#ffffff;
  --line:#dddddd;
}
*{margin:0;padding:0;box-sizing:border-box}
html,body{width:717px;height:1200px;overflow:hidden;background:var(--white)}
body{position:relative;font-family:"Open Sans",Arial,sans-serif;color:var(--ink)}
.abs{position:absolute}
.heading{font-family:"Raleway",Arial,sans-serif}

/* top bar */
.topbar{left:0;top:0;width:717px;height:17px;background:var(--blue);color:var(--white);font-size:7px;line-height:17px}
.topbar span{position:absolute;display:flex;align-items:center;gap:4px}
.flag{width:10px;height:7px;background:var(--blue-dark);border:1px solid #fff;position:relative}
.flag::after{content:"";position:absolute;left:0;right:0;top:2px;height:1.5px;background:#d22}

/* nav */
.nav{left:0;top:17px;width:717px;height:45px;background:var(--white);z-index:2}
.nav a{position:absolute;top:0;line-height:45px;font-family:"Raleway",sans-serif;font-weight:600;font-size:9px;color:var(--ink);text-decoration:none;letter-spacing:.2px}
.nav a.active{color:var(--orange)}
.brand{left:314px;top:3px;width:89px;height:106px;z-index:3}
.brand-name{left:314px;top:48px;width:89px;text-align:center;z-index:4;font-family:"Raleway",sans-serif;font-weight:700;font-size:10px;color:var(--ink);letter-spacing:.3px}

/* hero */
.hero{left:0;top:62px;width:717px;height:294px;background:linear-gradient(180deg,#2e7bc4 0%,#6aa6d8 38%,#e9e4da 62%,#d7cdb9 78%,#6a9a3a 100%)}
.hero-title{left:0;top:148px;width:717px;text-align:center;font-family:"Raleway",sans-serif;font-weight:800;font-size:47px;color:var(--white);text-shadow:0 2px 4px rgba(0,0,0,.35);letter-spacing:.5px}
.hero-sub{left:0;top:203px;width:717px;text-align:center;font-size:12.5px;color:var(--white);text-shadow:0 1px 3px rgba(0,0,0,.4)}
.btn{background:var(--orange);color:var(--white);border-radius:14px;font-family:"Raleway",sans-serif;font-weight:700;text-align:center;box-shadow:0 2px 3px rgba(0,0,0,.2)}
.hero-btn{left:295px;top:232px;width:128px;height:27px;line-height:27px;font-size:9.5px}
.dots{top:327px;height:2px;width:20px;background:var(--white)}

/* namaz bar */
.namaz{left:0;top:356px;width:717px;height:45px;background:var(--white);border-bottom:1px solid var(--line)}
.namaz-label{left:0;top:356px;width:160px;height:45px}
.namaz-col{top:356px;height:45px;text-align:center;font-size:8px}
.namaz-col b{display:block;margin-top:11px;font-family:"Raleway",sans-serif;font-weight:700;color:var(--ink)}
.namaz-col span{display:block;margin-top:2px;color:var(--muted)}
.divider{top:356px;width:1px;height:45px;background:var(--line)}

/* welcome */
.welcome-title{left:58px;top:441px;font-size:16px;font-weight:600;color:var(--ink)}
.welcome-text{left:58px;width:290px;font-size:6.7px;line-height:14.5px;color:var(--muted)}
.read-btn{left:58px;top:596px;width:82px;height:25px;line-height:25px;font-size:7.5px}
.video{left:370px;top:441px;width:288px;height:183px;background:linear-gradient(160deg,#c9b596 0%,#8c6e48 40%,#4a3826 75%,#2b2118 100%);border:1px solid #ccc}

/* services */
.services{left:0;top:666px;width:717px;height:248px;background:var(--light)}
.section-title{left:0;width:717px;text-align:center;font-size:16px;font-weight:600}
.service{top:736px;width:128px;height:146px;text-align:center}
.service svg.hex{position:absolute;left:0;top:0}
.service .icon{position:absolute;left:44px;top:26px}
.service h3{position:absolute;left:0;top:80px;width:128px;font-family:"Raleway",sans-serif;font-weight:600;font-size:11px;color:var(--ink)}
.service p{position:absolute;left:0;top:96px;width:128px;font-size:7px;color:var(--muted)}
.service .go{position:absolute;left:57px;top:113px}
.service.featured h3,.service.featured p{color:var(--white)}

/* contact */
.contact{left:0;top:914px;width:717px;height:248px;background:var(--blue)}
.contact-title{top:943px;color:var(--white)}
.sub-title{top:983px;font-size:11px;color:var(--white);font-weight:600;font-family:"Open Sans",sans-serif}
.field{background:var(--white);border:1px solid #cfd8e3;font-size:6.5px;color:var(--muted);padding:5px 7px;text-transform:uppercase}
.submit{left:377px;top:1111px;width:43px;height:19px;line-height:19px;font-size:7.5px;border-radius:10px}
.info-icon{left:468px;width:21px;height:21px}
.info-text{left:500px;font-size:7px;line-height:14px;color:var(--white)}

/* footer */
.footer{left:0;top:1162px;width:717px;height:38px;background:var(--white)}
.copy{left:58px;top:1176px;font-size:7px;color:var(--muted)}
.social{top:1172px;width:18px;height:18px;border-radius:50%}
</style>
</head>
<body>

<!-- top bar -->
<div class="abs topbar">
  <span style="left:58px">
    <svg width="8" height="6" viewBox="0 0 8 6"><rect width="8" height="6" fill="#fff"/><path d="M0 0 L4 3.5 L8 0" stroke="#1e6fbf" stroke-width="1" fill="none"/></svg>
    info@velmarudin.org
  </span>
  <span style="left:163px">
    <svg width="7" height="7" viewBox="0 0 10 10"><path d="M2 0 L4 3 L3 4 Q4 6 6 7 L7 6 L10 8 L8 10 Q3 9 0 2 Z" fill="#fff"/></svg>
    1 555 201 4730
  </span>
  <span style="left:622px"><i class="flag"></i>Eng
    <svg width="5" height="3" viewBox="0 0 5 3"><path d="M0 0 H5 L2.5 3Z" fill="#fff"/></svg>
  </span>
</div>

<!-- navigation -->
<nav class="abs nav">
  <a class="active" style="left:78px">HOME</a>
  <a style="left:141px">ABOUT</a>
  <a style="left:208px">PUBLICATIONS</a>
  <a style="left:435px">WELFARE</a>
  <a style="left:514px">EDUCATION</a>
  <a style="left:603px">BAYANAT</a>
</nav>
<svg class="abs brand" viewBox="0 0 89 106"><polygon points="44.5,1 88,26 88,80 44.5,105 1,80 1,26" fill="#fff" stroke="#e3e3e3" stroke-width="1"/></svg>
<div class="abs brand-name">VELMARUDIN</div>

<!-- hero -->
<div class="abs hero" role="img" aria-label="Photograph of a white marble mosque with a lattice dome, minaret and green gardens under a blue sky"></div>
<div class="abs hero-title">VELMARUDIN</div>
<div class="abs hero-sub">Lorem ipsum dolor sit amet, cod do eiusmod tem</div>
<div class="abs btn hero-btn">GET MORE INFO &gt;&gt;</div>
<div class="abs dots" style="left:335px"></div>
<div class="abs dots" style="left:361px"></div>
<div class="abs dots" style="left:387px"></div>

<!-- namaz timing -->
<div class="abs namaz"></div>
<svg class="abs namaz-label" viewBox="0 0 160 45">
  <polygon points="0,0 153,0 160,22.5 153,45 0,45" fill="#3ab54a"/>
  <circle cx="33" cy="22.5" r="10" fill="none" stroke="#fff" stroke-width="2.2"/>
  <path d="M33 16.5 V22.5 H38" stroke="#fff" stroke-width="2" fill="none"/>
  <text x="51" y="26" fill="#fff" font-family="Raleway, sans-serif" font-weight="700" font-size="10.5">NAMAZ TIMING</text>
</svg>
<div class="abs namaz-col" style="left:162px;width:80px"><b>FAJAR</b><span>6:25</span></div>
<div class="abs divider" style="left:245px"></div>
<div class="abs namaz-col" style="left:246px;width:90px"><b>ZAHUR</b><span>1:30</span></div>
<div class="abs divider" style="left:336px"></div>
<div class="abs namaz-col" style="left:337px;width:81px"><b>ASAR</b><span>4:30</span></div>
<div class="abs divider" style="left:418px"></div>
<div class="abs namaz-col" style="left:419px;width:94px"><b>MAGRIB</b><span>Sunset</span></div>
<div class="abs divider" style="left:513px"></div>
<div class="abs namaz-col" style="left:514px;width:83px"><b>ISHA</b><span>7:30</span></div>
<div class="abs divider" style="left:597px"></div>
<div class="abs namaz-col" style="left:598px;width:88px"><b>JUMMA</b><span>1:30</span></div>

<!-- welcome -->
<h1 class="abs heading welcome-title">WELCOME TO VELMARUDIN</h1>
<p class="abs welcome-text" style="top:475px">At vero eos et accusamus et iusto odio dignissimos ducimus qui blanditiis praesentium voluptatum deleniti atque corrupti quos dolore.</p>
<p class="abs welcome-text" style="top:519px">Quas molestias excepturi sint occaecati cupiditate non provident, similique sunt in cul pa qui officia deserunt mollitia animi, id est laborum et dolorum fuga. Et harum qdem rerum facilis est et expedita distinctio. Nam libero tempore, cum soluta nobis est elig endi optio cumque nihil impedit quo minus id quod.</p>
<div class="abs btn read-btn">READ MORE &gt;&gt;</div>
<div class="abs video" role="img" aria-label="Video still of worshippers gathered inside an ornate mosque hall"></div>
<svg class="abs" style="left:505px;top:524px" width="18" height="18" viewBox="0 0 18 18"><path d="M3 1 L17 9 L3 17 Z" fill="#fff"/></svg>

<!-- services -->
<div class="abs services"></div>
<h2 class="abs heading section-title" style="top:696px">OUR SERVICES</h2>

<div class="abs service featured" style="left:58px">
  <svg class="hex" width="128" height="146" viewBox="0 0 128 146"><polygon points="64,1 127,37 127,109 64,145 1,109 1,37" fill="#3ab54a"/></svg>
  <svg class="icon" width="40" height="44" viewBox="0 0 40 44"><rect x="13" y="2" width="14" height="24" rx="7" fill="none" stroke="#fff" stroke-width="3"/><path d="M7 20 Q7 33 20 33 Q33 33 33 20" fill="none" stroke="#fff" stroke-width="3"/><path d="M20 33 V40 M12 41 H28" stroke="#fff" stroke-width="3"/></svg>
  <h3>BAYANAT</h3><p>At vero eos et accusamu usto</p>
  <svg class="go" width="13" height="13" viewBox="0 0 13 13"><circle cx="6.5" cy="6.5" r="6.5" fill="#fff"/><path d="M5 3.5 L8 6.5 L5 9.5" stroke="#3ab54a" stroke-width="2" fill="none"/></svg>
</div>

<div class="abs service" style="left:215px">
  <svg class="hex" width="128" height="146" viewBox="0 0 128 146"><polygon points="64,1 127,37 127,109 64,145 1,109 1,37" fill="none" stroke="#3ab54a" stroke-width="1"/></svg>
  <svg class="icon" width="40" height="44" viewBox="0 0 40 44"><path d="M20 40 L4 22 Q-2 12 6 6 Q14 1 20 10 Q26 1 34 6 Q42 12 36 22 Z" fill="#3ab54a"/></svg>
  <h3>WELFARE</h3><p>At vero eos et accusamu usto</p>
  <svg class="go" width="13" height="13" viewBox="0 0 13 13"><circle cx="6.5" cy="6.5" r="6.5" fill="#3ab54a"/><path d="M5 3.5 L8 6.5 L5 9.5" stroke="#fff" stroke-width="2" fill="none"/></svg>
</div>

<div class="abs service" style="left:373px">
  <svg class="hex" width="128" height="146" viewBox="0 0 128 146"><polygon points="64,1 127,37 127,109 64,145 1,109 1,37" fill="none" stroke="#3ab54a" stroke-width="1"/></svg>
  <svg class="icon" width="40" height="44" viewBox="0 0 40 44"><path d="M11 4 H38 L32 36 H6 Z" fill="#3ab54a"/><path d="M6 36 Q2 36 3 40 H30 L31 38" fill="none" stroke="#3ab54a" stroke-width="3"/><path d="M15 12 H31 M14 18 H30" stroke="#fff" stroke-width="2"/></svg>
  <h3>PUBLICATIONS</h3><p>At vero eos et accusamu usto</p>
  <svg class="go" width="13" height="13" viewBox="0 0 13 13"><circle cx="6.5" cy="6.5" r="6.5" fill="#3ab54a"/><path d="M5 3.5 L8 6.5 L5 9.5" stroke="#fff" stroke-width="2" fill="none"/></svg>
</div>

<div class="abs service" style="left:530px">
  <svg class="hex" width="128" height="146" viewBox="0 0 128 146"><polygon points="64,1 127,37 127,109 64,145 1,109 1,37" fill="none" stroke="#3ab54a" stroke-width="1"/></svg>
  <svg class="icon" width="56" height="44" viewBox="0 0 56 44" style="left:36px"><path d="M28 6 L56 17 L28 28 L0 17 Z" fill="#3ab54a"/><path d="M13 22 V33 Q28 40 43 33 V22 L28 28 Z" fill="#3ab54a"/><path d="M6 19 V34" stroke="#3ab54a" stroke-width="2"/><rect x="4" y="33" width="4" height="7" fill="#3ab54a"/></svg>
  <h3>EDUCATION</h3><p>At vero eos et accusamu usto</p>
  <svg class="go" width="13" height="13" viewBox="0 0 13 13"><circle cx="6.5" cy="6.5" r="6.5" fill="#3ab54a"/><path d="M5 3.5 L8 6.5 L5 9.5" stroke="#fff" stroke-width="2" fill="none"/></svg>
</div>

<!-- contact -->
<div class="abs contact"></div>
<h2 class="abs heading section-title contact-title">CONTACT US</h2>
<div class="abs sub-title" style="left:58px">Get In Touch:</div>
<div class="abs field" style="left:59px;top:1009px;width:177px;height:19px">Name :</div>
<div class="abs field" style="left:243px;top:1009px;width:177px;height:19px">Phone :</div>
<div class="abs field" style="left:59px;top:1036px;width:177px;height:19px">Email :</div>
<div class="abs field" style="left:243px;top:1036px;width:177px;height:19px">Company :</div>
<div class="abs field" style="left:59px;top:1061px;width:361px;height:43px">Message :</div>
<div class="abs btn submit">SUBMIT</div>

<div class="abs sub-title" style="left:467px">Contact Information</div>
<svg class="abs info-icon" style="top:1008px" viewBox="0 0 21 21"><circle cx="10.5" cy="10.5" r="10" fill="none" stroke="#fff"/><path d="M10.5 5 Q7 5 7 8.5 Q7 11 10.5 15.5 Q14 11 14 8.5 Q14 5 10.5 5Z" fill="#fff"/><circle cx="10.5" cy="8.5" r="1.3" fill="#1e6fbf"/></svg>
<div class="abs info-text" style="top:1009px">212 W. Linden Park Rd. Suite 118,<br>Fairview, CA 92810</div>
<svg class="abs info-icon" style="top:1046px" viewBox="0 0 21 21"><circle cx="10.5" cy="10.5" r="10" fill="none" stroke="#fff"/><path d="M7 6 L9 8.5 L8.2 9.5 Q9.5 11.8 11.5 12.8 L12.5 12 L15 14 L13.5 15.5 Q8.5 14.5 5.5 7.5 Z" fill="#fff"/></svg>
<div class="abs info-text" style="top:1050px">555 201 4730</div>
<svg class="abs info-icon" style="top:1075px" viewBox="0 0 21 21"><circle cx="10.5" cy="10.5" r="10" fill="none" stroke="#fff"/><rect x="6" y="7" width="9" height="8" fill="#fff"/><rect x="8" y="5" width="5" height="3" fill="#fff"/><path d="M8 10 H13 M8 12.5 H13" stroke="#1e6fbf"/></svg>
<div class="abs info-text" style="top:1079px">555 201 4731</div>
<svg class="abs info-icon" style="top:1105px" viewBox="0 0 21 21"><circle cx="10.5" cy="10.5" r="10" fill="none" stroke="#fff"/><rect x="6" y="7" width="9" height="7" fill="#fff"/><path d="M6 7 L10.5 11 L15 7" stroke="#1e6fbf" fill="none"/></svg>
<div class="abs info-text" style="top:1109px">info@velmarudin.org</div>

<!-- footer -->
<footer class="abs footer"></footer>
<div class="abs copy">Copyrights © 2016, Velmarudin. All Rights Reserved.</div>
<div class="abs social" style="left:578px;background:#2d4f8e"></div>
<div class="abs social" style="left:598px;background:#2aa3e0"></div>
<div class="abs social" style="left:619px;background:#e0463a"></div>

</body>
</html>
```